Recruiting Flyer

We need a flyer created for our real estate company, BrightHearth.com. I have supplied a basic version of the flyer we would like turned into a creative print piece to hand out to perspective agents. We would like to see designs that use the color pantones we provide. The final design should communicate our modern new age company providing better tools and services than the competition.

Industry/Entity Type

Real Estate

```html
<!DOCTYPE html>
<html lang="en">
<head>
<meta charset="utf-8">
<title>BrightHearth.com – Your Career Connection</title>
<link href="https://fonts.googleapis.com/css2?family=Open+Sans:wght@300;400;700&family=Roboto+Condensed:wght@400&display=swap" rel="stylesheet">
<style>
  :root {
    --brand-blue: #1c3ee0;
    --brand-green: #6ed61e;
    --brand-orange: #f2380c;
    --text-grey: #6b6f73;
    --heading-grey: #707478;
    --paper: #ffffff;
    --photo-light: #d9c7b6;
    --photo-mid: #9c7a64;
    --photo-dark: #4a3a33;
  }
  * { margin: 0; padding: 0; box-sizing: border-box; }
  html, body { width: 900px; height: 1200px; overflow: hidden; background: var(--paper); }
  .flyer {
    position: relative;
    width: 900px;
    height: 1200px;
    overflow: hidden;
    background: var(--paper);
    font-family: "Open Sans", Arial, sans-serif;
  }
  .hero-photo {
    position: absolute;
    left: 0; top: 0;
    width: 900px; height: 600px;
    background:
      radial-gradient(ellipse 260px 300px at 500px 260px, var(--photo-light), transparent 70%),
      linear-gradient(135deg, var(--photo-mid) 0%, var(--photo-dark) 45%, var(--photo-mid) 75%, var(--photo-light) 100%);
  }
  .hero-curves {
    position: absolute;
    left: 0; top: 0;
    width: 900px; height: 600px;
  }
  .brand-name {
    position: absolute;
    left: 58px; top: 40px;
    font-family: "Open Sans", Arial, sans-serif;
    font-weight: 700;
    font-size: 38px;
    letter-spacing: -0.5px;
    color: var(--brand-blue);
  }
  .headline {
    position: absolute;
    left: 57px; top: 474px;
    font-weight: 700;
    font-size: 36px;
    line-height: 50px;
    letter-spacing: 0.5px;
  }
  .headline .line-blue { color: var(--brand-blue); display: block; }
  .headline .line-green { color: var(--brand-green); display: block; }
  .column {
    position: absolute;
    top: 628px;
  }
  .column.say-no { left: 55px; }
  .column.say-yes { left: 487px; }
  .column-title {
    font-weight: 300;
    font-size: 36px;
    color: var(--heading-grey);
    margin-bottom: 26px;
    white-space: nowrap;
  }
  .column-title strong { font-weight: 700; }
  .say-no .column-title strong { color: var(--brand-orange); }
  .say-yes .column-title strong { color: var(--brand-blue); }
  .point-list { list-style: none; }
  .point-list li {
    display: flex;
    align-items: center;
    height: 40.5px;
    font-weight: 400;
    font-size: 18px;
    color: var(--text-grey);
    white-space: nowrap;
  }
  .say-no .point-list { margin-left: 33px; }
  .say-yes .point-list { margin-left: 33px; }
  .point-icon { width: 24px; height: 24px; margin-right: 16px; flex: none; }
  .call-to-action {
    position: absolute;
    top: 1098px;
    font-family: "Roboto Condensed", "Arial Narrow", sans-serif;
    font-size: 25px;
    line-height: 27px;
    text-align: right;
    letter-spacing: -0.5px;
  }
  .call-to-action .green { color: var(--brand-green); display: block; }
  .call-to-action .blue { color: var(--brand-blue); display: block; }
  .cta-join { right: 423px; }
  .cta-careers { right: 68px; }
</style>
</head>
<body>
<div class="flyer">
  <div class="hero-photo" role="img" aria-label="Photo of a cheering group of smiling professionals pointing toward the viewer"></div>
  <svg class="hero-curves" viewBox="0 0 900 600" aria-hidden="true">
    <path d="M0,0 L610,0 C470,70 250,150 0,152 Z" fill="var(--paper)"/>
    <path d="M0,352 C220,330 390,520 560,543 C700,560 820,420 900,368 L900,600 L0,600 Z" fill="var(--brand-orange)"/>
    <path d="M0,378 C220,360 390,548 560,565 C700,578 820,450 900,400 L900,600 L0,600 Z" fill="var(--brand-green)"/>
    <path d="M0,410 C220,392 390,572 560,584 C700,594 820,478 900,438 L900,600 L0,600 Z" fill="var(--paper)"/>
  </svg>

  <div class="brand-name">BrightHearth.com</div>

  <h1 class="headline">
    <span class="line-blue">Your Career</span>
    <span class="line-green">Connection</span>
  </h1>

  <section class="column say-no">
    <h2 class="column-title">Say <strong>NO</strong> to:</h2>
    <ul class="point-list">
      <li><svg class="point-icon" viewBox="0 0 24 24"><circle cx="12" cy="12" r="10.5" fill="none" stroke="var(--brand-orange)" stroke-width="1.5"/><path d="M8.5 8.5 L15.5 15.5 M15.5 8.5 L8.5 15.5" stroke="var(--brand-orange)" stroke-width="2.2" stroke-linecap="round"/></svg>Desk Fees</li>
      <li><svg class="point-icon" viewBox="0 0 24 24"><circle cx="12" cy="12" r="10.5" fill="none" stroke="var(--brand-orange)" stroke-width="1.5"/><path d="M8.5 8.5 L15.5 15.5 M15.5 8.5 L8.5 15.5" stroke="var(--brand-orange)" stroke-width="2.2" stroke-linecap="round"/></svg>Franchise Fees</li>
      <li><svg class="point-icon" viewBox="0 0 24 24"><circle cx="12" cy="12" r="10.5" fill="none" stroke="var(--brand-orange)" stroke-width="1.5"/><path d="M8.5 8.5 L15.5 15.5 M15.5 8.5 L8.5 15.5" stroke="var(--brand-orange)" stroke-width="2.2" stroke-linecap="round"/></svg>Hidden Fees</li>
      <li><svg class="point-icon" viewBox="0 0 24 24"><circle cx="12" cy="12" r="10.5" fill="none" stroke="var(--brand-orange)" stroke-width="1.5"/><path d="M8.5 8.5 L15.5 15.5 M15.5 8.5 L8.5 15.5" stroke="var(--brand-orange)" stroke-width="2.2" stroke-linecap="round"/></svg>Mandatory Meetings</li>
      <li><svg class="point-icon" viewBox="0 0 24 24"><circle cx="12" cy="12" r="10.5" fill="none" stroke="var(--brand-orange)" stroke-width="1.5"/><path d="M8.5 8.5 L15.5 15.5 M15.5 8.5 L8.5 15.5" stroke="var(--brand-orange)" stroke-width="2.2" stroke-linecap="round"/></svg>Mandatory Scheduled Training</li>
      <li><svg class="point-icon" viewBox="0 0 24 24"><circle cx="12" cy="12" r="10.5" fill="none" stroke="var(--brand-orange)" stroke-width="1.5"/><path d="M8.5 8.5 L15.5 15.5 M15.5 8.5 L8.5 15.5" stroke="var(--brand-orange)" stroke-width="2.2" stroke-linecap="round"/></svg>Building Someone Else’s Brand</li>
      <li><svg class="point-icon" viewBox="0 0 24 24"><circle cx="12" cy="12" r="10.5" fill="none" stroke="var(--brand-orange)" stroke-width="1.5"/><path d="M8.5 8.5 L15.5 15.5 M15.5 8.5 L8.5 15.5" stroke="var(--brand-orange)" stroke-width="2.2" stroke-linecap="round"/></svg>Leads given to chosen few</li>
      <li><svg class="point-icon" viewBox="0 0 24 24"><circle cx="12" cy="12" r="10.5" fill="none" stroke="var(--brand-orange)" stroke-width="1.5"/><path d="M8.5 8.5 L15.5 15.5 M15.5 8.5 L8.5 15.5" stroke="var(--brand-orange)" stroke-width="2.2" stroke-linecap="round"/></svg>Minimum Commission Rates</li>
      <li><svg class="point-icon" viewBox="0 0 24 24"><circle cx="12" cy="12" r="10.5" fill="none" stroke="var(--brand-orange)" stroke-width="1.5"/><path d="M8.5 8.5 L15.5 15.5 M15.5 8.5 L8.5 15.5" stroke="var(--brand-orange)" stroke-width="2.2" stroke-linecap="round"/></svg>Expensive Tools</li>
    </ul>
  </section>

  <section class="column say-yes">
    <h2 class="column-title">Say <strong>YES</strong> To:</h2>
    <ul class="point-list">
      <li><svg class="point-icon" viewBox="0 0 24 24"><circle cx="12" cy="12" r="10.5" fill="none" stroke="var(--brand-blue)" stroke-width="1.5"/><path d="M7.5 12.5 L10.8 15.5 L16.5 8.5" fill="none" stroke="var(--brand-blue)" stroke-width="2.2" stroke-linecap="round" stroke-linejoin="round"/></svg>Innovative Virtual Model</li>
      <li><svg class="point-icon" viewBox="0 0 24 24"><circle cx="12" cy="12" r="10.5" fill="none" stroke="var(--brand-blue)" stroke-width="1.5"/><path d="M7.5 12.5 L10.8 15.5 L16.5 8.5" fill="none" stroke="var(--brand-blue)" stroke-width="2.2" stroke-linecap="round" stroke-linejoin="round"/></svg>Revenue sharing</li>
      <li><svg class="point-icon" viewBox="0 0 24 24"><circle cx="12" cy="12" r="10.5" fill="none" stroke="var(--brand-blue)" stroke-width="1.5"/><path d="M7.5 12.5 L10.8 15.5 L16.5 8.5" fill="none" stroke="var(--brand-blue)" stroke-width="2.2" stroke-linecap="round" stroke-linejoin="round"/></svg>Aggressive compensation</li>
      <li><svg class="point-icon" viewBox="0 0 24 24"><circle cx="12" cy="12" r="10.5" fill="none" stroke="var(--brand-blue)" stroke-width="1.5"/><path d="M7.5 12.5 L10.8 15.5 L16.5 8.5" fill="none" stroke="var(--brand-blue)" stroke-width="2.2" stroke-linecap="round" stroke-linejoin="round"/></svg>Weekly coaching</li>
      <li><svg class="point-icon" viewBox="0 0 24 24"><circle cx="12" cy="12" r="10.5" fill="none" stroke="var(--brand-blue)" stroke-width="1.5"/><path d="M7.5 12.5 L10.8 15.5 L16.5 8.5" fill="none" stroke="var(--brand-blue)" stroke-width="2.2" stroke-linecap="round" stroke-linejoin="round"/></svg>Training when &amp; how you want it</li>
      <li><svg class="point-icon" viewBox="0 0 24 24"><circle cx="12" cy="12" r="10.5" fill="none" stroke="var(--brand-blue)" stroke-width="1.5"/><path d="M7.5 12.5 L10.8 15.5 L16.5 8.5" fill="none" stroke="var(--brand-blue)" stroke-width="2.2" stroke-linecap="round" stroke-linejoin="round"/></svg>Everyone knows your name</li>
      <li><svg class="point-icon" viewBox="0 0 24 24"><circle cx="12" cy="12" r="10.5" fill="none" stroke="var(--brand-blue)" stroke-width="1.5"/><path d="M7.5 12.5 L10.8 15.5 L16.5 8.5" fill="none" stroke="var(--brand-blue)" stroke-width="2.2" stroke-linecap="round" stroke-linejoin="round"/></svg>Leads given to those qualified</li>
      <li><svg class="point-icon" viewBox="0 0 24 24"><circle cx="12" cy="12" r="10.5" fill="none" stroke="var(--brand-blue)" stroke-width="1.5"/><path d="M7.5 12.5 L10.8 15.5 L16.5 8.5" fill="none" stroke="var(--brand-blue)" stroke-width="2.2" stroke-linecap="round" stroke-linejoin="round"/></svg>Negotiating the best rate</li>
      <li><svg class="point-icon" viewBox="0 0 24 24"><circle cx="12" cy="12" r="10.5" fill="none" stroke="var(--brand-blue)" stroke-width="1.5"/><path d="M7.5 12.5 L10.8 15.5 L16.5 8.5" fill="none" stroke="var(--brand-blue)" stroke-width="2.2" stroke-linecap="round" stroke-linejoin="round"/></svg>Free cutting edge Technology</li>
    </ul>
  </section>

  <div class="call-to-action cta-join">
    <span class="green">Join Our Team</span>
    <span class="blue">Call Today</span>
  </div>
  <div class="call-to-action cta-careers">
    <span class="green">Careers With BrightHearth</span>
    <span class="blue">###-###-####</span>
  </div>
</div>
</body>
</html>
```